Adapt logo for box truck wrap for my restoration company

I need a wrap for our company Brightway Restoration. We specialize in water damage restoration. I’ve attached our logo, business card, and page header. Things I would like to include are- 24 hour emergency service, our phone number (555)014-7392 and that we do water, fire and mold work. It’s a 2004 Kardella Vonter which I’ve attached pictures of. I will get the cab wrapped as well.

Industry/Entity Type

Construction- specifically Restoration

Font styles to use
Sans Serif

Colors

Designer to choose colors to be used in the design.

Requirements
Must have
• Water• Fire• Mold, phone number (555)014-7392
Nice to have
• Clean, professional look with the logo

```html
<!DOCTYPE html>
<html lang="en">
<head>
<meta charset="utf-8">
<title>Brightway Restoration – Box Truck Wrap Sides</title>
<link rel="stylesheet" href="https://fonts.googleapis.com/css2?family=Oswald:wght@500;600;700&display=swap">
<style>
  :root {
    --wrap-blue: #3a8bcd;
    --wrap-gray: #808080;
    --wrap-white: #ffffff;
    --page-bg: #ffffff;
    --water-light: #d9eef8;
    --water-mid: #7fbde3;
    --fire-orange: #f07a22;
    --fire-yellow: #f7b733;
  }
  * { margin: 0; padding: 0; box-sizing: border-box; }
  html, body {
    width: 1200px;
    height: 1200px;
    overflow: hidden;
    background: var(--page-bg);
  }
  .wrap-sheet {
    width: 1200px;
    height: 1200px;
    display: flex;
    flex-direction: column;
    align-items: center;
    justify-content: center;
    gap: 80px;
  }
  .box-side {
    display: block;
    width: 1080px;
    height: 480px;
  }
  .panel-bg { fill: var(--wrap-blue); }
  .service-band { fill: var(--wrap-gray); }
  .logo-disc { fill: var(--wrap-white); }
  .brand-small {
    font-family: "Oswald", sans-serif;
    font-weight: 500;
    fill: var(--wrap-white);
    font-size: 21px;
  }
  .brand-large {
    font-family: "Oswald", sans-serif;
    font-weight: 700;
    fill: var(--wrap-gray);
    text-anchor: middle;
  }
  .badge-ring { fill: none; stroke: var(--wrap-white); stroke-width: 6; }
  .hour-text {
    font-family: "Oswald", sans-serif;
    font-weight: 700;
    fill: var(--wrap-white);
  }
  .clock-face { fill: none; stroke: var(--wrap-white); stroke-width: 2; }
  .clock-hand { stroke: var(--wrap-white); stroke-width: 1.6; stroke-linecap: round; }
  .service-text {
    font-family: "Oswald", sans-serif;
    font-weight: 600;
    fill: var(--wrap-white);
    font-size: 27px;
  }
  .phone-arc {
    font-family: "Oswald", sans-serif;
    font-weight: 700;
    fill: var(--wrap-blue);
    font-size: 27px;
    letter-spacing: 3px;
  }
</style>
</head>
<body>
<main class="wrap-sheet">

  <!-- Driver side: brand left, large circle right -->
  <svg class="box-side box-side--driver" viewBox="0 0 765 340" xmlns="http://www.w3.org/2000/svg">
    <defs>
      <clipPath id="driver-clip"><rect width="765" height="340"/></clipPath>
      <linearGradient id="splash-driver" x1="0" y1="0" x2="0" y2="1">
        <stop offset="0" stop-color="var(--wrap-blue)"/>
        <stop offset="0.45" stop-color="var(--water-mid)"/>
        <stop offset="0.7" stop-color="var(--water-light)"/>
        <stop offset="0.85" stop-color="var(--fire-yellow)"/>
        <stop offset="1" stop-color="var(--fire-orange)"/>
      </linearGradient>
      <path id="phone-path-driver" d="M477,36 A172,172 0 0 0 477,304"/>
    </defs>
    <g clip-path="url(#driver-clip)">
      <rect class="panel-bg" width="765" height="340"/>
      <rect class="splash-art" x="0" y="185" width="480" height="155" fill="url(#splash-driver)" role="img" aria-label="Water splash rising over flames"/>
      <rect class="service-band" x="0" y="135" width="400" height="50"/>
      <text class="service-text" x="46" y="171">WATER• FIRE• MOLD</text>

      <g class="brand-lockup">
        <circle class="badge-ring" cx="58" cy="58" r="36"/>
        <text class="brand-small" x="112" y="50">BRIGHTWAY</text>
        <text class="brand-small" x="112" y="82">RESTORATION</text>
      </g>

      <g class="emergency-badge" transform="translate(311,10)">
        <circle class="clock-face" cx="58" cy="14" r="12"/>
        <line class="clock-hand" x1="58" y1="14" x2="58" y2="7"/>
        <line class="clock-hand" x1="58" y1="14" x2="64" y2="17"/>
        <text class="hour-text" x="0" y="44" font-size="22">24HOUR</text>
        <text class="hour-text" x="1" y="55" font-size="7.2">EMERGENCY SERVICE</text>
      </g>

      <circle class="logo-disc" cx="585" cy="170" r="195"/>
      <text class="phone-arc"><textPath href="#phone-path-driver" startOffset="50%" text-anchor="middle">(555)014-7392</textPath></text>
      <text class="brand-large" x="610" y="165" font-size="52">BRIGHTWAY</text>
      <text class="brand-large" x="610" y="212" font-size="36">RESTORATION</text>
    </g>
  </svg>

  <!-- Passenger side: large circle left, brand right -->
  <svg class="box-side box-side--passenger" viewBox="0 0 765 340" xmlns="http://www.w3.org/2000/svg">
    <defs>
      <clipPath id="passenger-clip"><rect width="765" height="340"/></clipPath>
      <linearGradient id="splash-passenger" x1="0" y1="0" x2="0" y2="1">
        <stop offset="0" stop-color="var(--wrap-blue)"/>
        <stop offset="0.45" stop-color="var(--water-mid)"/>
        <stop offset="0.7" stop-color="var(--water-light)"/>
        <stop offset="0.85" stop-color="var(--fire-yellow)"/>
        <stop offset="1" stop-color="var(--fire-orange)"/>
      </linearGradient>
      <path id="phone-path-passenger" d="M281,309 A172,172 0 0 0 276,27"/>
    </defs>
    <g clip-path="url(#passenger-clip)">
      <rect class="panel-bg" width="765" height="340"/>
      <rect class="splash-art" x="280" y="185" width="485" height="155" fill="url(#splash-passenger)" role="img" aria-label="Water splash rising over flames"/>
      <rect class="service-band" x="368" y="135" width="397" height="50"/>
      <text class="service-text" x="412" y="171">WATER• FIRE• MOLD</text>

      <g class="emergency-badge" transform="translate(365,10)">
        <circle class="clock-face" cx="58" cy="14" r="12"/>
        <line class="clock-hand" x1="58" y1="14" x2="58" y2="7"/>
        <line class="clock-hand" x1="58" y1="14" x2="64" y2="17"/>
        <text class="hour-text" x="0" y="44" font-size="22">24HOUR</text>
        <text class="hour-text" x="1" y="55" font-size="7.2">EMERGENCY SERVICE</text>
      </g>

      <g class="brand-lockup">
        <circle class="badge-ring" cx="572" cy="58" r="36"/>
        <text class="brand-small" x="626" y="50">BRIGHTWAY</text>
        <text class="brand-small" x="626" y="82">RESTORATION</text>
      </g>

      <circle class="logo-disc" cx="180" cy="170" r="195"/>
      <text class="phone-arc"><textPath href="#phone-path-passenger" startOffset="50%" text-anchor="middle">(555)014-7392</textPath></text>
      <text class="brand-large" x="150" y="165" font-size="52">BRIGHTWAY</text>
      <text class="brand-large" x="150" y="212" font-size="36">RESTORATION</text>
    </g>
  </svg>

</main>
</body>
</html>
```